Peter Lasko-Wren Finance

Need a personal website advertising Equipment Finance,Business Finance,Commercial Finance, Construction Finance, Bridging Finance. Similar websites are www.varoplend.com.au / www.kitmoxa.com.au / www.rzb4.com.au /wwwbelvaxcredit.com.au

Target Market(s)

Business People

Industry/Entity Type

Business

Number of Pages Required

3 page

Font styles to use
Serif
Sans Serif

Requirements
Must have
• All i want is a simple corporate looking website advertising Equipment Finance, Commercial Finance, Construction Finance, Business Finance, Bridging Finance,

```html
<!DOCTYPE html>
<html lang="en">
<head>
<meta charset="utf-8">
<title>Peter Lasko-Wren Finance</title>
<link href="https://fonts.googleapis.com/css2?family=Mulish:wght@300;400;600&family=Open+Sans:ital,wght@1,400&display=swap" rel="stylesheet">
<style>
:root{
  --blue:#3ba9dc;
  --footer:#42abdd;
  --orange:#ff8a00;
  --ink:#333a40;
  --text:#6b6f73;
  --grey-bg:#f3f3f3;
  --line:#dcdcdc;
  --dark-btn:#444444;
  --white:#ffffff;
}
*{box-sizing:border-box;margin:0;padding:0}
html,body{width:1200px;height:2571px;overflow:hidden}
body{position:relative;background:var(--white);font-family:"Mulish",sans-serif;color:var(--ink)}
.abs{position:absolute}

/* header */
.site-header{left:0;top:0;width:1200px;height:98px;background:var(--white)}
.brand{left:120px;top:32px;font-size:25px;font-weight:400;color:var(--blue);letter-spacing:.3px}
.brand span{color:var(--orange)}
.main-nav{left:448px;top:38px;display:flex;gap:27px;font-size:16.5px;color:var(--text)}
.nav-phone{left:916px;top:33px;display:flex;align-items:center;gap:7px;font-size:17px;color:var(--text)}

/* hero */
.hero{left:0;top:98px;width:1200px;height:543px;
  background:linear-gradient(100deg,#4f7fbf 0%,#6d9ad0 22%,#8a8f7a 40%,#c9a53a 52%,#7a96c2 66%,#5d88c6 82%,#3d5f8d 100%)}
.hero-kicker{left:118px;top:347px;font-size:22px;font-weight:600;color:var(--white);letter-spacing:.6px}
.hero-title{left:118px;top:378px;font-size:41px;font-weight:400;color:var(--white);letter-spacing:.5px}
.hero-dots{left:552px;top:607px;display:flex;gap:8px}
.hero-dots i{width:14px;height:14px;border-radius:50%;background:var(--white)}
.hero-dots i.current{background:transparent;border:2px solid var(--white)}

.quote-box{left:766px;top:223px;width:312px;height:281px;background:var(--orange);padding:27px 27px 0}
.quote-box h2{font-size:26px;font-weight:400;color:var(--white)}
.quote-box p{margin-top:8px;font-size:13px;line-height:18px;color:#fff3e2;width:250px}
.quote-field{display:block;width:264px;height:34px;margin-top:12px;background:var(--white);font-size:12.5px;color:#a5a5a5;padding:9px 14px}
.quote-box .quote-field:first-of-type{margin-top:20px}
.quote-submit{display:block;margin-top:12px;width:129px;height:39px;background:var(--dark-btn);color:var(--white);font-size:17px;line-height:39px;text-align:center}

/* services */
.section-title{font-size:29px;font-weight:400;color:var(--ink)}
.services-title{left:0;top:682px;width:1200px;text-align:center}
.title-rule{top:702px;width:52px;height:1px;background:#c9c9c9}
.title-rule::after{content:"";position:absolute;top:-3px;width:7px;height:7px;border-radius:50%;background:#c9c9c9}
.title-rule.left{left:372px}.title-rule.left::after{right:0}
.title-rule.right{left:788px}.title-rule.right::after{left:0}
.service-list{left:128px;top:783px;display:flex}
.service{width:186px;height:155px;text-align:center;border-right:1px solid var(--line);padding-top:30px}
.service:last-child{border-right:none}
.service svg{display:block;margin:0 auto;height:52px}
.service h3{margin-top:16px;font-size:17px;font-weight:400;line-height:22px;color:var(--text)}

/* about */
.about{left:0;top:1034px;width:1200px;height:432px;background:var(--grey-bg);border-top:1px solid var(--line);border-bottom:1px solid var(--line)}
.about-photo{left:0;top:1035px;width:620px;height:430px;
  background:linear-gradient(90deg,#b9a692 0%,#d8cbbf 25%,#e3ebef 50%,#eef1f2 75%,var(--grey-bg) 100%)}
.about-title{left:612px;top:1121px}
.about-text{left:612px;top:1174px;width:478px;font-size:13.5px;line-height:20px;color:var(--text)}
.about-text p+p{margin-top:14px}
.btn{display:inline-block;border-radius:20px;color:var(--white);font-size:12px;text-align:center;letter-spacing:.3px}
.btn-orange{background:var(--orange)}
.btn-blue{background:var(--blue)}
.about-btn{left:610px;top:1353px;width:132px;height:38px;line-height:38px}

/* promo cards */
.card{top:1524px;width:468px;height:243px;border:1px solid #cfcfcf;background:var(--white)}
.card-team{left:120px}.card-finance{left:602px}
.card-photo{left:0;top:0;width:254px;height:241px;clip-path:polygon(0 0,74% 0,100% 100%,0 100%)}
.card-team .card-photo{background:linear-gradient(135deg,#c6b3a0,#e6ddd3 55%,#bfae9e)}
.card-finance .card-photo{background:linear-gradient(160deg,#8fb7e3 0%,#c9d6e1 45%,#9d8a72 100%)}
.card-body{left:263px;top:26px;width:185px}
.card-body h3{font-size:22px;font-weight:400}
.card-team h3{color:var(--blue)}.card-finance h3{color:var(--orange)}
.card-body p{margin-top:10px;font-size:13.5px;line-height:20px;color:var(--text)}
.card-body p+p{margin-top:8px}
.card-btn{left:263px;top:180px;width:110px;height:32px;line-height:32px;font-size:11.5px}

/* testimonial */
.testimonial{left:0;top:1850px;width:1200px;height:377px;background:var(--grey-bg);border-top:1px solid var(--line)}
.testimonial-title{left:0;top:1889px;width:1200px;text-align:center}
.quote-card{left:309px;top:1988px;width:591px;height:189px;background:var(--white);border:1px solid #e2e2e2;text-align:center;padding-top:52px}
.quote-card blockquote{font-family:"Open Sans",sans-serif;font-style:italic;font-size:15.5px;line-height:26px;color:var(--text);width:530px;margin:0 auto}
.quote-card cite{display:block;margin-top:8px;font-style:normal;font-size:16px;color:var(--blue)}
.stars{margin-top:2px;font-size:19px;color:var(--orange);letter-spacing:1px}
.avatar{border-radius:50%;border:3px solid var(--white)}
.avatar-small{width:60px;height:60px;top:1955px;background:linear-gradient(160deg,#7b7b7b,#c9c9c9)}
.avatar-left{left:498px}.avatar-right{left:644px}
.avatar-main{left:556px;top:1934px;width:94px;height:94px;background:linear-gradient(160deg,#6e5a48,#c7a78a);box-shadow:0 0 0 2px #e4e4e4}
.slider-arrow{top:2052px}

/* footer */
.site-footer{left:0;top:2227px;width:1200px;height:344px;background:var(--footer);color:var(--white)}
.footer-col{top:58px}
.footer-col h4{font-size:22px;font-weight:400;margin-bottom:18px}
.footer-col li{list-style:none;font-size:13px;line-height:29px}
.footer-col.contact li{line-height:25px}
.social{display:flex;gap:4px;margin-top:-2px}
.social i{width:30px;height:30px;border-radius:50%;border:1.5px solid var(--white)}
.footer-rule{left:149px;top:269px;width:902px;height:1px;background:#6cbde4}
.copyright{left:0;top:298px;width:1200px;text-align:center;font-size:13px;color:#d6eef9}
</style>
</head>
<body>

<header class="site-header abs">
  <div class="brand abs">Peter Lasko-Wren <span>Finance</span></div>
  <nav class="main-nav abs"><span>About</span><span>Financing Services</span><span>How it works</span><span>Support</span></nav>
  <div class="nav-phone abs">
    <svg width="18" height="18" viewBox="0 0 24 24"><path fill="#3ba9dc" d="M6.6 10.8a15.2 15.2 0 0 0 6.6 6.6l2.2-2.2c.3-.3.7-.4 1-.2 1.1.4 2.3.6 3.6.6.6 0 1 .4 1 1V20c0 .6-.4 1-1 1A17 17 0 0 1 3 4c0-.6.4-1 1-1h3.5c.6 0 1 .4 1 1 0 1.3.2 2.5.6 3.6.1.3 0 .7-.2 1z"/></svg>
    <span>61 7 5550 1234</span>
  </div>
</header>

<section class="hero abs" role="img" aria-label="Photo looking up at tower cranes and high-rise buildings under construction against a blue sky"></section>
<div class="hero-kicker abs">FUSCE ULTRICIES ORCI FEUGIAT</div>
<h1 class="hero-title abs">COMMERCIAL FINANCE</h1>
<div class="hero-dots abs"><i class="current"></i><i></i><i></i><i></i></div>

<form class="quote-box abs">
  <h2>Get a Quote Now</h2>
  <p>Class aptent taciti sociosqu ad litora torquent per conubia nost</p>
  <span class="quote-field">Name</span>
  <span class="quote-field">Email address</span>
  <span class="quote-submit">Submit</span>
</form>

<h2 class="section-title services-title abs">What Services we provide</h2>
<span class="title-rule left abs"></span><span class="title-rule right abs"></span>

<div class="service-list abs">
  <div class="service">
    <svg viewBox="0 0 60 52" width="60"><rect x="4" y="14" width="52" height="34" rx="4" fill="#3ba9dc"/><path d="M21 14V8h18v6" fill="none" stroke="#3ba9dc" stroke-width="4"/><rect x="4" y="27" width="52" height="3" fill="#fff"/><rect x="26" y="24" width="8" height="8" fill="#3ba9dc" stroke="#fff" stroke-width="2"/></svg>
    <h3>Business<br>Finance</h3>
  </div>
  <div class="service">
    <svg viewBox="0 0 70 60" width="70"><g fill="none" stroke="#3ba9dc" stroke-width="2.5"><rect x="8" y="8" width="40" height="30" rx="4"/><rect x="16" y="16" width="24" height="14"/><path d="M48 18h14v10H48M28 38v16M20 54h16M8 28H2"/></g></svg>
    <h3>Equipment<br>Finance</h3>
  </div>
  <div class="service">
    <svg viewBox="0 0 70 60" width="70"><g fill="#3ba9dc"><rect x="4" y="20" width="18" height="38"/><rect x="24" y="2" width="22" height="56"/><rect x="48" y="14" width="18" height="44"/></g><g fill="#fff"><rect x="29" y="8" width="5" height="6"/><rect x="37" y="8" width="5" height="6"/><rect x="29" y="20" width="5" height="6"/><rect x="37" y="20" width="5" height="6"/><rect x="29" y="32" width="5" height="6"/><rect x="37" y="32" width="5" height="6"/><rect x="31" y="46" width="8" height="12"/><rect x="9" y="28" width="8" height="6"/><rect x="9" y="40" width="8" height="6"/><rect x="53" y="22" width="8" height="6"/><rect x="53" y="34" width="8" height="6"/></g></svg>
    <h3>Commercial<br>Finance</h3>
  </div>
  <div class="service">
    <svg viewBox="0 0 70 60" width="70"><g fill="none" stroke="#3ba9dc" stroke-width="3"><path d="M22 36V4l28 14M22 4l-8 10h8M50 18v10"/><path d="M46 28h8l-2 5h-4z" fill="#3ba9dc"/></g><rect x="10" y="34" width="36" height="10" fill="#3ba9dc"/><rect x="8" y="46" width="44" height="10" rx="5" fill="#3ba9dc"/><g fill="#fff"><circle cx="15" cy="51" r="2.5"/><circle cx="24" cy="51" r="2.5"/><circle cx="33" cy="51" r="2.5"/><circle cx="42" cy="51" r="2.5"/></g></svg>
    <h3>Construction<br>Finance</h3>
  </div>
  <div class="service">
    <svg viewBox="0 0 80 52" width="80"><g fill="none" stroke="#3ba9dc" stroke-width="3"><path d="M2 44h76M6 14c14 14 54 14 68 0M6 10v34M74 10v34M18 22v22M30 26v18M40 27v17M50 26v18M62 22v22M6 34c10-10 58-10 68 0"/></g></svg>
    <h3>Bridging<br>Finance</h3>
  </div>
</div>

<section class="about abs"></section>
<div class="about-photo abs" role="img" aria-label="Photo of three businesswomen meeting around a table with a laptop and papers, fading into the grey background"></div>
<h2 class="section-title about-title abs">Do You Want Start a Business?</h2>
<div class="about-text abs">
  <p>Mr. Peter Lasko-Wren serves as Operations Director of Harlow Financial services Pty Ltd. Mr. Lasko-Wren has 16 years experience in the Financial Services and bridging Finance industry, both in Australia, as well as in South Africa. He was employed by the South African based business (BRIGHT MERIDIAN FINANCE) for the majority of its operation.</p>
  <p>He held senior operational positions within Bright Meridian Finance and provided staff support and direction, training and operational</p>
</div>
<span class="btn btn-orange about-btn abs">READ MORE</span>

<article class="card card-team abs">
  <div class="card-photo abs" role="img" aria-label="Photo of a team of colleagues gathered around a desk"></div>
  <div class="card-body abs">
    <h3>Our Team</h3>
    <p>Praesent elementum elit at tellus nec ultricies sit</p>
    <p>Amet porttitor mattis enim In massa libero interdum nec interdum vel blandit</p>
  </div>
  <span class="btn btn-blue card-btn abs">READ MORE</span>
</article>
<article class="card card-finance abs">
  <div class="card-photo abs" role="img" aria-label="Photo of a building under construction with a crane against a bright sky"></div>
  <div class="card-body abs">
    <h3>Get Finance Now</h3>
    <p>Praesent elementum elit at tellus nec ultricies sit</p>
    <p>Amet porttitor mattis enim In massa libero interdum nec interdum vel blandit</p>
  </div>
  <span class="btn btn-orange card-btn abs">READ MORE</span>
</article>

<section class="testimonial abs"></section>
<h2 class="section-title testimonial-title abs">Testimonial</h2>
<div class="quote-card abs">
  <blockquote>Aommodo a mi Morbi ornare gravida elit Integer congue augue et malesuada iaculis ipsum dui aliquet felis at cursus magna</blockquote>
  <cite>By Author Name</cite>
  <div class="stars">★★★★</div>
</div>
<div class="avatar avatar-small avatar-left abs" role="img" aria-label="Client portrait photo"></div>
<div class="avatar avatar-small avatar-right abs" role="img" aria-label="Client portrait photo"></div>
<div class="avatar avatar-main abs" role="img" aria-label="Featured client portrait photo"></div>
<svg class="slider-arrow abs" style="left:262px" width="24" height="36" viewBox="0 0 24 36"><path d="M20 2L4 18l16 16" fill="none" stroke="#a9a9a9" stroke-width="3"/></svg>
<svg class="slider-arrow abs" style="left:918px" width="24" height="36" viewBox="0 0 24 36"><path d="M4 2l16 16L4 34" fill="none" stroke="#a9a9a9" stroke-width="3"/></svg>

<footer class="site-footer abs">
  <div class="footer-col abs" style="left:149px"><h4>Company</h4><ul><li>About Us</li><li>Why We Are</li><li>How it Works</li><li>Support</li></ul></div>
  <div class="footer-col abs" style="left:319px"><h4>Services</h4><ul><li>Equipment Finance</li><li>Business Finance</li><li>Commercial Finance</li><li>Construction Finance</li><li>Bridging Finance</li></ul></div>
  <div class="footer-col abs" style="left:514px"><h4>Resources</h4><ul><li>Support</li><li>FAQ</li><li>Testimonials</li><li>Contact Us</li></ul></div>
  <div class="footer-col contact abs" style="left:684px"><h4>Contact Us</h4><ul><li>14 Tidewater Parade</li><li>Coral Bay, Queensland 4299</li><li>Australia</li><li>Phone: 61 7 5550 1234</li><li>Fax: 61 7 5550 1299</li></ul></div>
  <div class="footer-col abs" style="left:943px"><h4>Follow Us</h4><div class="social"><i></i><i></i><i></i><i></i></div></div>
  <div class="footer-rule abs"></div>
  <div class="copyright abs">© 2017 Company Name&nbsp; All right reserved&nbsp; Term of Use</div>
</footer>

</body>
</html>
```